Website/Logo redesign: PlayfieldHub.com

We need a web design for a sports social network.
We have already built the web-site but are unhappy with the current design.
We like colours that evoke outdoors, eg sky blue and grass green.
Please see how it currently looks:
http://www.playfieldhub.example/6ce7bfd2fe66ba012a2a5e5217e2d776/
We are happy for everything to change, including logo, icons etc or for you to keep anything you think will work with your new design.
Updates
Project Deadline Extended
Reason: We have not yet found the design we are happy with so will be providing more feedback and extending the deadine.
We have increased the budget and also agreed to pay a second place award.
I will be giving existing and any new designs feedback daily.
Target Market(s)
Our target audience are mainly young sports players, but also older ones too.
Industry/Entity Type
Social
Look and feel
Each slider illustrates characteristics of the customer's brand and the style your logo design should communicate.

```html
<!DOCTYPE html>
<html lang="en">
<head>
<meta charset="utf-8">
<title>PlayfieldHub – Headlines</title>
<link href="https://fonts.googleapis.com/css2?family=Oswald:wght@400&family=Roboto+Condensed:wght@700&family=Arimo:wght@400;700&family=Cousine&display=swap" rel="stylesheet">
<style>
:root{
  --nav-green:#8db20f;
  --nav-active:#f4e41c;
  --dark-panel:#1c2708;
  --panel-line:#3a4a12;
  --slate:#646e96;
  --slate-text:#5e6894;
  --ink:#0c1a3a;
  --light-panel:#f2f2f2;
  --white:#ffffff;
  --rsvp-yellow:#f0d21a;
  --tick-green:#7cc21e;
  --highlight:#646e96;
}
*{box-sizing:border-box;margin:0;padding:0}
html,body{width:1200px;height:960px;overflow:hidden}
body{position:relative;font-family:"Arimo",Arial,sans-serif;color:var(--ink)}
.abs{position:absolute}
.backdrop{inset:0;background:
  linear-gradient(180deg,#6f84a8 0%,#9aa4bd 25%,#c9b9a9 45%,#b6a58f 62%,#8fa24a 85%,#5f8c1e 100%)}
.brand{left:202px;top:20px;font-family:"Oswald",sans-serif;font-size:27px;letter-spacing:1px;color:var(--white)}
.sign-in{left:926px;top:45px;font-family:"Arimo",sans-serif;font-weight:700;font-size:13px;color:var(--white)}
.nav{left:202px;top:70px;width:797px;height:54px;background:var(--nav-green)}
.nav ul{list-style:none;display:flex;position:absolute;left:15px;top:12px;font-family:"Roboto Condensed",sans-serif;font-size:17px;color:var(--white)}
.nav li:nth-child(1){width:131px;color:var(--nav-active)}
.nav li:nth-child(2){width:119px}
.nav li:nth-child(3){width:133px}
.nav li:nth-child(4){width:120px}
.nav li:nth-child(5){width:97px}
.nav li:nth-child(6){width:117px}
.search{left:803px;top:103px;width:125px;height:21px;background:var(--dark-panel);color:var(--rsvp-yellow);font-size:11px;font-weight:700;padding:4px 6px}
.search svg{position:absolute;right:4px;top:4px}
.go{left:928px;top:103px;width:45px;height:21px;background:var(--dark-panel);color:var(--white);font-size:11px;font-weight:700;text-align:center;line-height:21px}
.hero{left:202px;top:124px;width:576px;height:345px;background:linear-gradient(135deg,#c9d4dd 0%,#d98a40 35%,#c65a24 55%,#7a6a30 75%,#3f4a2a 100%)}
.edit-btn{background:var(--white);border:1px solid #bbb;font-size:12.5px;padding:2px 7px;color:var(--ink)}
.edit-cover{left:623px;top:364px}
.sidebar{left:780px;top:124px;width:219px;height:337px;background:var(--dark-panel);border:3px solid var(--panel-line)}
.fixture-card{height:44px;border-bottom:3px solid var(--panel-line);padding:3px 8px;color:var(--white);font-size:10.5px;font-weight:700;line-height:14px}
.fixture-card .meta{display:flex;justify-content:space-between;color:var(--rsvp-yellow);font-weight:400}
.feed-title{color:var(--white);font-size:10.5px;font-weight:700;padding:4px 6px}
.feed-item{display:flex;gap:6px;padding:2px 8px 6px;font-size:8.5px;color:var(--white);line-height:12px;height:61px}
.thumb{flex:none;width:56px;height:38px;background:linear-gradient(135deg,#9fb6d0,#d07a3a)}
.feed-item b{display:block;color:var(--rsvp-yellow);font-size:10.5px;font-weight:400}
.feed-item .rsvp{color:var(--rsvp-yellow)}
.strip{left:202px;top:469px;width:797px;height:7px;background:var(--nav-green)}
.profile-head{left:202px;top:476px;width:588px;height:43px;background:var(--slate);color:var(--white);font-weight:700;font-size:13px;padding:14px 24px}
.col-left{left:202px;top:519px;width:226px;height:402px;background:var(--light-panel)}
.col-mid{left:447px;top:519px;width:342px;height:402px;background:var(--light-panel)}
.avatar{left:214px;top:530px;width:181px;height:116px;background:linear-gradient(135deg,#4d7fc0,#e2733a 60%,#4a8cd0)}
.edit-profile{left:356px;top:596px;font-weight:700}
.stats{left:215px;top:657px;width:179px;height:28px;background:var(--white);border:1px solid #ccc;display:flex;font-size:11px;padding:2px 6px;line-height:12px}
.stats div{width:44px}
.box-btn{background:var(--white);border:2px solid #ddd;font-weight:700;font-size:13px;color:var(--ink);padding:3px 8px}
.create{left:214px;top:705px}
.teams{left:215px;top:761px;width:179px;height:108px;background:var(--white);border:1px solid #ccc;padding:4px 5px;font-size:11px;line-height:17px;color:var(--ink)}
.teams b{font-size:12.5px}
.label-tab{background:var(--white);border:1px solid #ccc;font-weight:700;font-size:13px;color:var(--ink);padding:4px 13px;width:138px}
.next-tab{left:459px;top:526px}
.match{font-size:12.5px;line-height:15px}
.match .title{color:var(--slate-text);font-weight:700;font-size:13.5px}
.next-match{left:460px;top:557px}
.rsvp-line{color:var(--slate-text);font-weight:700}
.rsvp-line span{color:var(--ink);font-weight:400}
.dot{display:inline-block;width:8px;height:8px;border-radius:50%;margin:0 2px 0 4px}
.divider{left:457px;top:611px;width:323px;height:2px;background:#ddd}
.activity{left:459px;top:628px;width:319px;height:182px;background:var(--white);border:1px solid #ccc;padding:10px 12px}
.act{display:flex;gap:5px;height:53px;font-size:9px;line-height:16px;position:relative}
.act .thumb{width:56px;height:37px}
.act b{display:block;color:var(--slate-text);font-size:13px;line-height:14px}
.act .ago{position:absolute;right:0;top:38px;font-weight:700;font-size:10px}
.last-tab{left:459px;top:823px}
.last-match{left:458px;top:854px}
.quote-head,.league-head{background:var(--slate);color:var(--white);border:3px solid var(--white);text-align:center;font-weight:700;font-size:13.5px}
.quote-box{left:801px;top:476px;width:198px;height:212px;background:var(--light-panel)}
.quote-head{height:38px;line-height:32px}
.quote-text{font-family:"Cousine",monospace;font-size:10.5px;line-height:18px;padding:9px 8px;color:var(--ink)}
.quote-by{text-align:right;padding-right:24px;font-family:"Roboto Condensed",sans-serif;font-size:12px;margin-top:-4px}
.league-box{left:801px;top:701px;width:198px;height:213px;background:var(--light-panel)}
.league-head{height:38px;line-height:14px;padding-top:3px}
.league-head small{font-weight:400;font-size:12px}
.league-table{margin:12px 0 0 6px;border-collapse:collapse;font-size:13px;width:182px}
.league-table td{height:27px}
.league-table .hl span{background:var(--highlight);color:var(--white);padding:1px 3px}
.num{text-align:right;width:26px}
</style>
</head>
<body>
<div class="abs backdrop" role="img" aria-label="Stadium sky at dusk over a grass pitch with a football"></div>

<div class="abs brand">PLAYFIELD HUB</div>
<div class="abs sign-in">SIGN IN</div>

<nav class="abs nav"><ul><li>HEADLINES</li><li>MY STATS</li><li>CHALLNGRS</li><li>FIXTURES</li><li>TEAMS</li><li>LEAGUES</li><li>TOOLS</li></ul></nav>
<div class="abs search">Search Players
  <svg width="14" height="13" viewBox="0 0 14 13"><circle cx="5" cy="5" r="3.5" fill="none" stroke="#f0d21a" stroke-width="2"/><line x1="8" y1="8" x2="13" y2="12" stroke="#f0d21a" stroke-width="2.5"/></svg>
</div>
<div class="abs go">GO</div>

<div class="abs hero" role="img" aria-label="Cover photo of young footballers celebrating a goal"></div>
<div class="abs edit-btn edit-cover">Edit Cover Picture</div>

<aside class="abs sidebar">
  <div class="fixture-card">U15 Football Team Vs Colossians House<div class="meta"><span>RSVP: Available</span><span>29th July</span></div></div>
  <div class="fixture-card">U15 Football Team Vs Colossians House<div class="meta"><span>RSVP: Available</span><span>30th July</span></div></div>
  <div class="fixture-card">U15 Football Team Vs Colossians House<div class="meta"><span>RSVP: Available</span><span>5th Aug</span></div></div>
  <div class="feed-title">NEWS FEED</div>
  <div class="feed-item"><div class="thumb" role="img" aria-label="Player photo"></div><div><b>JAMIE CORWIN</b>Lorem Ipsum is simply dummy text of the printing<br><strong>Sunday, 29th July, 1PM</strong><br><span class="rsvp">RSVP: ✓ ✕</span></div></div>
  <div class="feed-item"><div class="thumb" role="img" aria-label="Player photo"></div><div><b>SAM STEDLEY</b>Lorem Ipsum is simply dummy text of the printing<br><strong>Friday, 4th Aug, 1PM</strong><br><span class="rsvp">RSVP: ✓ ✕</span></div></div>
  <div class="feed-item"><div class="thumb" role="img" aria-label="Player photo"></div><div><b>SAM STEDLEY</b>Lorem Ipsum is simply dummy text of the printing<br><span class="rsvp">RSVP: ✓ ✕</span></div></div>
</aside>

<div class="abs strip"></div>
<div class="abs profile-head">LEO HARTWELL</div>
<div class="abs col-left"></div>
<div class="abs col-mid"></div>

<div class="abs avatar" role="img" aria-label="Profile photo of a boy kicking a football"></div>
<div class="abs edit-btn edit-profile">Edit Profile</div>
<div class="abs stats"><div><b>24</b><br>Played</div><div style="width:64px"><b>3</b><br>Teams</div><div><b>7</b><br>Awards</div></div>
<div class="abs box-btn create">Create New Fixture</div>
<div class="abs teams"><b>All Teams</b><br>U15 FOOTBALL TEAM B<br>GALATIANS HOUSE<br>U15 RUGBY TEAM<br>GALATIANS HOUSE<br>U15 RUGBY TEAM</div>

<div class="abs label-tab next-tab">Next Fixture</div>
<div class="abs match next-match"><div class="title">U15 FOOTBALL TEAM VS COLOSSIANS</div>Sunday, 29th July, 1PM<br>
  <span class="rsvp-line">RSVP:<span class="dot" style="background:var(--tick-green)"></span><span>Available</span><span class="dot" style="border:1px solid #ccc"></span><span>Unavailable</span></span></div>
<div class="abs divider"></div>

<div class="abs activity">
  <div class="act"><div class="thumb" role="img" aria-label="Player photo"></div><div><b>ADRIAN SORREL</b>Lorem Ipsum is simply dummy text of the printing<br>and typesetting industry.</div><span class="ago">2m ago</span></div>
  <div class="act"><div class="thumb" role="img" aria-label="Player photo"></div><div><b>JAMIE CORWIN</b>Lorem Ipsum is simply dummy text of the printing<br>and typesetting industry.</div><span class="ago">1hr ago</span></div>
  <div class="act"><div class="thumb" role="img" aria-label="Player photo"></div><div><b>SAM STEDLEY</b>Lorem Ipsum is simply dummy text of the printing<br>and typesetting industry.</div><span class="ago">45m ago</span></div>
</div>

<div class="abs label-tab last-tab">Last Result</div>
<div class="abs match last-match"><div class="title">WESTBROOK VALE VS HARTLEY U15</div>Friday, 27th July, 1PM</div>

<section class="abs quote-box">
  <div class="quote-head">QUOTE OF THE DAY</div>
  <p class="quote-text">Lorem Ipsum is simply dummy text of the printing and typesetting industry. Lorem Ipsum has been the industry's standard dummy text ever since the 1500s, when an unknown printer took a galley.</p>
  <div class="quote-by">MARCUS ALDEN</div>
</section>

<section class="abs league-box">
  <div class="league-head">LEAGUE TABLE<br><small>Westbrook Inter House Football</small></div>
  <table class="league-table">
    <tr><td>1 Colossians</td><td class="num">12</td><td class="num">36</td></tr>
    <tr><td>2 Phillipans</td><td class="num">12</td><td class="num">30</td></tr>
    <tr class="hl"><td>3 <span>Galatians</span></td><td class="num">11</td><td class="num">12</td></tr>
    <tr><td>4 Romans</td><td class="num">12</td><td class="num">4</td></tr>
    <tr><td>5 Corinthans</td><td class="num">11</td><td class="num">1</td></tr>
  </table>
</section>
</body>
</html>
```